Webdesign mit Grundfarbe Weinrot für allgemeine Steuerberatung
Zielgruppe
Allgemeine Steuerberatung. Zielgruppe ist breit gefächert, allerdings soll die Webseite eher den Jungunternehmer ansprechen.
Aufgabenstellung
Die Grundfarbe sollte weinrot sein.

```html
<!DOCTYPE html>
<html lang="de">
<head>
<meta charset="utf-8">
<title>Steuerberatung k1vra</title>
<link href="https://fonts.googleapis.com/css2?family=Raleway:wght@400;500;600;700&display=swap" rel="stylesheet">
<style>
:root{
  --wine:#6a0d23;
  --wine-soft:rgba(110,50,62,.88);
  --ink:#2a2a2a;
  --text:#4a4a4a;
  --muted:#8a8a8a;
  --line:#e6e6e6;
  --grey-bg:#f5f4f4;
  --white:#ffffff;
}
*{box-sizing:border-box;margin:0;padding:0}
html,body{width:1200px;height:731px;overflow:hidden;background:var(--white);font-family:"Raleway",sans-serif;color:var(--text)}
.page{width:1200px;height:731px;position:relative}
.container{width:860px;margin:0 auto;position:relative}

.site-header{height:62px;border-bottom:1px solid var(--line)}
.site-header .container{height:62px;display:flex;justify-content:space-between;align-items:center}
.brand{display:flex;align-items:center;gap:8px;font-weight:700;color:var(--ink);font-size:17px}
.brand-mark{width:14px;height:14px;background:var(--wine)}
.brand small{display:block;font-size:17px}
.header-right{text-align:right}
.contact-line{font-size:11px;color:var(--ink);display:flex;align-items:center;gap:5px;justify-content:flex-end}
.contact-hours{font-size:8px;color:var(--muted);margin-top:2px}
.main-nav{display:flex;gap:22px;margin-top:10px;font-size:12px}
.main-nav a{color:var(--muted);text-decoration:none}
.main-nav a.active{color:var(--ink);font-weight:600}

.hero{height:240px;position:relative}
.hero-photo{position:absolute;inset:0;background:linear-gradient(90deg,#cfc4b8 0%,#dcd2c7 40%,#c9b4a6 70%,#b89a8a 100%)}
.hero-arrow{position:absolute;left:170px;top:102px;width:22px;height:36px;background:rgba(255,255,255,.6);display:flex;align-items:center;justify-content:center}
.hero-title{position:absolute;left:270px;top:94px;color:var(--white)}
.hero-title span{display:inline-block;background:var(--wine-soft);padding:4px 10px;font-size:19px;font-weight:400}
.hero-title strong{display:inline-block;background:var(--wine-soft);padding:4px 10px;font-size:19px;font-weight:600}

.about{height:172px;padding-top:26px}
.about .container{display:flex;gap:28px;width:720px}
.about-photo{width:240px;height:122px;flex:none;background:linear-gradient(135deg,#d9dde2,#b9c0c9)}
.section-title{font-size:17px;font-weight:500;color:var(--ink);margin-bottom:8px}
.about p{font-size:9.5px;line-height:1.6;margin-bottom:8px}

.services{height:128px;background:var(--grey-bg);text-align:center;padding-top:16px}
.services h2{font-size:13px;font-weight:600;color:var(--ink)}
.services-sub{font-size:8px;color:var(--muted);margin-top:3px}
.service-list{display:flex;justify-content:center;gap:70px;margin-top:16px}
.service{font-size:9px;color:var(--text);display:flex;flex-direction:column;align-items:center;gap:6px}

.cta{height:129px;background:var(--wine);color:var(--white);text-align:center;padding-top:26px}
.cta h2{font-size:16px;font-weight:700}
.cta p{font-size:9px;line-height:1.5;margin:6px auto 12px;width:330px;opacity:.9}
.cta-button{display:inline-block;background:#e9e6e6;color:var(--ink);font-size:8px;letter-spacing:.5px;padding:5px 12px;text-transform:uppercase}
</style>
</head>
<body>
<div class="page">
  <header class="site-header">
    <div class="container">
      <div class="brand"><span class="brand-mark"></span><span>Marlene k1vra</span></div>
      <div class="header-right">
        <div class="contact-line">
          <svg width="11" height="11" viewBox="0 0 24 24"><path d="M6.6 10.8a15 15 0 0 0 6.6 6.6l2.2-2.2a1 1 0 0 1 1-.25 11 11 0 0 0 3.6.6 1 1 0 0 1 1 1V20a1 1 0 0 1-1 1A17 17 0 0 1 3 4a1 1 0 0 1 1-1h3.5a1 1 0 0 1 1 1 11 11 0 0 0 .6 3.6 1 1 0 0 1-.25 1z" fill="#2a2a2a"/></svg>
          +49 (0)8100-472031
        </div>
        <div class="contact-hours">Mo–Do 8–18 Uhr / Fr 8–13 Uhr</div>
        <nav class="main-nav">
          <a class="active" href="#">Start</a><a href="#">Leistungen</a><a href="#">Über uns</a><a href="#">Aktuelles</a><a href="#">Kontakt</a>
        </nav>
      </div>
    </div>
  </header>

  <section class="hero">
    <div class="hero-photo" role="img" aria-label="Foto einer lächelnden Beraterin mit Brille im Büro"></div>
    <div class="hero-arrow"><svg width="8" height="12" viewBox="0 0 8 12"><path d="M6 1 1 6l5 5" stroke="#555" stroke-width="2" fill="none"/></svg></div>
    <h1 class="hero-title"><span>Wilkommen bei der</span><br><strong>Steuerberatung k1vra</strong></h1>
  </section>

  <section class="about">
    <div class="container">
      <div class="about-photo" role="img" aria-label="Foto von zwei Mitarbeiterinnen am Schreibtisch mit Laptop"></div>
      <div>
        <h2 class="section-title">Über uns</h2>
        <p>Meine Kanzlei berät seit deren Gründung im Jahre 2003 Freiberufler, Gewerbetreibende, Kapitalgesellschaften, Personengesellschaften aus den verschiedensten Branchen sowie gemeinnützige Organisationen. Ebenso unterstützen wir gerne Existenzgründer und nebenberuflich Tätige, wie auch Arbeitnehmer, Vermieter und Rentner.</p>
        <p>Mein Team aus erfahrenen Steuerfachangestellten und ich freuen uns, Ihnen kompetent und individuell auf Ihre persönlichen Bedürfnisse abgestimmt, bei Ihren steuerlichen Angelegenheiten zu helfen!</p>
      </div>
    </div>
  </section>

  <section class="services">
    <h2>Leistungen</h2>
    <div class="services-sub">Leistungsumfang unserer Kanzlei für Sie in der Übersicht</div>
    <div class="service-list">
      <div class="service"><svg width="22" height="24" viewBox="0 0 22 24"><rect x="3" y="2" width="16" height="20" fill="none" stroke="#444" stroke-width="2"/><path d="M7 8h8M7 12h8M7 16h5" stroke="#444" stroke-width="2"/></svg>Buchführung</div>
      <div class="service"><svg width="22" height="24" viewBox="0 0 22 24"><rect x="2" y="4" width="13" height="18" fill="none" stroke="#444" stroke-width="2"/><path d="M7 2h13v16" fill="none" stroke="#444" stroke-width="2"/></svg>Lohnabrechnungen</div>
      <div class="service"><svg width="22" height="24" viewBox="0 0 22 24"><rect x="3" y="2" width="16" height="20" fill="none" stroke="#444" stroke-width="2"/><path d="M7 17V13M11 17V9M15 17v-6" stroke="#444" stroke-width="2"/></svg>Jahresabschluss</div>
      <div class="service"><svg width="22" height="24" viewBox="0 0 22 24"><rect x="3" y="2" width="16" height="20" fill="none" stroke="#444" stroke-width="2"/><circle cx="10" cy="11" r="3" fill="none" stroke="#444" stroke-width="2"/><path d="M12 13l4 4" stroke="#444" stroke-width="2"/></svg>Steuererklärungen</div>
    </div>
  </section>

  <section class="cta">
    <h2>Können wir Ihnen weiterhelfen?</h2>
    <p>Gerne beantworten wir Ihre Fragen und vereinbaren mit Ihnen einen Termin. Sie können uns anrufen oder eine Nachricht schreiben.</p>
    <a class="cta-button">Kontaktformular</a>
  </section>
</div>
</body>
</html>
```